Flyer for a martial arts school

Require a marketing flyer for martial arts school www.velkorfightacademy.com.au

Design should be synergistic with website and include relevant contact information including phone, location and email.

Needs to include key benefits for martial arts such as self defence, fitness, loss weight, confidence.

Also include a section for a new offer each time. For example the first will be "First Lesson Is Free" - similar to the file attached, but a more sophisticated look and feel.

Have attached several logos types plus photos on my website too.

Industry/Entity Type

Marketing

Requirements
Must have
• double sided and either A5 or DL whichever we think will give the best ability to get the message across.
• Design should be synergistic with website and include relevant contact information including phone, location and email www.velkorfightacademy.com.au
• Needs to include key benefits for martial arts such as self defence, fitness, loss weight, confidence.
• Also include a section for a new offer each time. For example the first will be "First Lesson Is Free" - similar to the file attached, but a more sophisticated look and feel....and a limited call to action, in that the free lesson is for the month of March.
• Have attached several logos types plus photos on my website too.
• Front could include:
• ​images
• Free lesson offer as the header
• Testimonials from Facebook​
• I have trained with Marcus for well over a decade. Not only is he a very good martial artist, but an even better person. Marcus is passionate about the martial arts and that comes through in his teaching. You are in very good hands at Velkor.​...Trevor Pollard, Head Trainer, Granite Martial Arts
• Marcus Pellman is a great motivator and leader, and has been personally selected by me to teach the Riverbend Ju Jitsu system....Glen Warrington, Founder Riverbend Martial Arts
• Address for Facebook https://www.facebook.com/Velkorfightacademy
• The second side could be used for:
• larger logo
• location (potentially a map?)
• A statement along the lines of "If you know someone who would like to join you, they can have a free lesson too"
• Information about Velkor
• Velkor Fight Academy programs are designed for adults and children of all ages..a safe, enjoyable and empowering way to learn self defence and martial arts.
• If you feel that you would like to:
• start on a remarkable journey and learn street-smart self-defence from trainers just like you.
• benefit from a high-energy, high-intensity workout and
• become more centred and present in everyday life
• ...take up our offer of a free introductory class at the top of the page or give us a call, we cant wait to meet you.

```html
<!DOCTYPE html>
<html lang="en">
<head>
<meta charset="utf-8">
<title>Velkor Fight Academy – Flyer</title>
<link rel="stylesheet" href="https://fonts.googleapis.com/css2?family=Arimo:wght@400;700&family=Play:wght@700&display=swap">
<style>
  :root {
    --backdrop: #15171c;
    --paper: #ffffff;
    --navy: #1b1f6e;
    --navy-deep: #131658;
    --gold: #c1962c;
    --gold-soft: #f7e9bf;
    --cream: #fbf3dc;
    --red: #d81f26;
    --map-tone: #ece5d8;
  }
  * { margin: 0; padding: 0; box-sizing: border-box; }
  html, body { width: 1200px; height: 1000px; overflow: hidden; background: var(--backdrop); }
  body { font-family: "Arimo", Arial, sans-serif; font-weight: 700; }
  .flyer { position: absolute; left: 248px; top: 0; width: 704px; height: 1000px; background: var(--paper); overflow: hidden; }
  .waves { position: absolute; inset: 0; }
  .abs { position: absolute; }

  .brand { left: 20px; top: 12px; display: flex; align-items: center; gap: 14px; }
  .brand-mark { width: 106px; height: 106px; border-radius: 50%; background: var(--navy); border: 6px solid var(--gold); }
  .brand-name { color: var(--navy); font-size: 40px; line-height: 1; letter-spacing: 1px; }

  .what-is { left: 502px; top: 155px; width: 137px; height: 41px; background: var(--navy-deep); border: 3px solid var(--gold);
    color: #fff; font-size: 16px; display: flex; align-items: center; justify-content: center; }

  .intro { left: 31px; top: 207px; width: 670px; color: var(--gold); font-size: 16.2px; line-height: 21px; }
  .intro strong { color: var(--navy); font-size: 19px; }

  .benefits { font-family: "Play", sans-serif; color: var(--navy); }
  .b-confidence { left: 192px; top: 294px; font-size: 24px; letter-spacing: 0.8px; }
  .b-martial { left: 338px; top: 292px; font-size: 25px; color: var(--gold); font-family: "Arimo", sans-serif; }
  .b-fitness { left: 465px; top: 295px; font-size: 23px; }
  .b-weight { left: 295px; top: 332px; font-size: 16px; font-family: "Arimo", sans-serif; }
  .b-loss { left: 358px; top: 327px; font-size: 21px; font-family: "Arimo", sans-serif; }
  .b-arts { left: 413px; top: 325px; font-size: 25px; color: var(--gold); font-family: "Arimo", sans-serif; }
  .b-defence { left: 496px; top: 331px; font-size: 20px; letter-spacing: 1.2px; font-family: "Arimo", sans-serif; }

  .lead { left: 24px; top: 375px; color: var(--navy); font-size: 20px; line-height: 26px; }
  .lead span { display: inline-block; margin-left: 42px; border-bottom: 3px solid var(--navy); padding: 0 10px 3px 0; }

  .point { color: var(--gold); font-size: 17px; line-height: 22px; text-align: center; }
  .point-journey { left: 26px; top: 469px; width: 200px; }
  .point-workout { left: 307px; top: 466px; width: 270px; text-align: left; }
  .point-workout .in { padding-left: 26px; }

  .athlete { left: 230px; top: 452px; width: 70px; height: 192px; border-radius: 35px 35px 10px 10px;
    background: linear-gradient(180deg, #e9e9ee, #cfd0d8); }

  .offer { left: 289px; top: 560px; color: var(--navy); font-size: 20px; line-height: 24px; }
  .offer .big { display: block; font-size: 25px; margin-top: 6px; margin-left: -12px; }

  .map { left: 122px; top: 681px; width: 345px; height: 183px; border: 3px solid var(--navy-deep); background: var(--map-tone); }

  .address { left: 484px; top: 681px; color: var(--gold); font-size: 16px; line-height: 20px; font-style: normal; }
  .phone { left: 484px; top: 814px; color: var(--gold); font-size: 16px; line-height: 20px; }
  .web { left: 121px; top: 870px; color: var(--gold); font-size: 15px; }

  .referral { left: 0; width: 704px; top: 934px; text-align: center; color: var(--red); font-size: 17px; line-height: 26px; }
  .referral b { font-size: 21px; }
</style>
</head>
<body>
<main class="flyer">
  <svg class="waves" width="704" height="1000" viewBox="0 0 704 1000" aria-hidden="true">
    <defs>
      <linearGradient id="headBand" x1="0" y1="0" x2="0" y2="1">
        <stop offset="0" stop-color="#ffffff"/>
        <stop offset="1" stop-color="#1b1f6e"/>
      </linearGradient>
      <linearGradient id="creamBand" x1="0" y1="0" x2="0" y2="1">
        <stop offset="0" stop-color="#f9ebc0"/>
        <stop offset="1" stop-color="#ffffff"/>
      </linearGradient>
    </defs>
    <path d="M0 80 H704 V140 C560 110 420 130 260 150 C150 162 60 165 0 160 Z" fill="url(#headBand)"/>
    <path d="M0 240 C150 275 350 262 520 265 C610 267 670 250 704 240 V560 C640 470 540 400 420 380 C300 360 200 330 0 300 Z" fill="url(#creamBand)" opacity="0.8"/>
    <path d="M0 930 C180 895 420 880 704 895 V940 C480 925 250 930 0 965 Z" fill="url(#creamBand)" opacity="0.9"/>
  </svg>

  <header class="abs brand">
    <div class="brand-mark"></div>
    <div class="brand-name">Velkor Fight Academy</div>
  </header>

  <div class="abs what-is">What is Velkor?</div>

  <p class="abs intro"><strong>Velkor Fight Academy</strong> programs are designed for adults and children of all ages.<br>A safe, enjoyable and empowering way to learn self defence and martial arts.</p>

  <div class="benefits">
    <span class="abs b-confidence">Confidence</span>
    <span class="abs b-martial">MARTIAL</span>
    <span class="abs b-fitness">Fitness</span>
    <span class="abs b-weight">Weight</span>
    <span class="abs b-loss">Loss</span>
    <span class="abs b-arts">ARTS</span>
    <span class="abs b-defence">SELF DEFENCE</span>
  </div>

  <p class="abs lead">If you feel that<br><span>you would like to:</span></p>

  <p class="abs point point-journey">Start on a remarkable<br>journey and learn<br>street-smart<br>self-defence from<br>trainers just like you.</p>
  <div class="abs athlete" role="img" aria-label="Photo of a student in a white uniform and black belt mid-kick"></div>
  <p class="abs point point-workout">Benefit from a high-energy,<br><span class="in">high-intensity workout and</span><br>present in everyday life</p>

  <p class="abs offer">Take up our offer of a free<br>introductory class or give us a call.<span class="big">We can’t wait to meet you!</span></p>

  <div class="abs map" role="img" aria-label="Street map showing the academy location upstairs at Halden gym"></div>

  <address class="abs address">Upstairs @Halden<br>48 Carrow St,<br>Ashfield<br>NSW 2131</address>
  <p class="abs phone">Ashfield<br>+02 8123 4567</p>
  <p class="abs web">www.velkorfightacademy.com.au</p>

  <p class="abs referral">"If you know someone who would like to join you,<br>they can have a <b>free lesson</b> too"</p>
</main>
</body>
</html>
```